Set of ads for a Medical Clinic in Costa Blanca Spain

We will start a small medical clinic for general medicine for Swedish and Scandinavians living on Costa Blanca Spain.
The clinic is called BrovaClinic
We need a set of ads with different sizes and also looking for a Designer to work with longtime.

Sizes of the adds:
One add with size 95 mm x 128 mm
One add with size 192 x 128 mm

We want one version of the add with a sign across the add "Öppnar i November" meaning "Opening in November" That add will be like a teaser and just creating attention to the clinic.

Skandinavisk Vårdcentral Costa Blanca

- Hembesök/Mobil Vårdcentral
- Lättakut
- Uppföljning av blodtryck, diabetes

Läs mer och boka din tid enkelt på www.brovaclinic-demo.com
Hitta hit:
Kliniken ligger utmed N418 vid Playa Serenita, mitt emot Lorvista
Av. Tomás Herrera 7-2, 03412 Valmira Costa

I have added pixelharbor images that could be used if you want, also open for other suggestions.

Target Market(s)

Swedish and Scandinavian patients looking for medical care in Spain

Industry/Entity Type

Medical

Colors
33b8a4
33a6d7
85cae6

Requirements
Must have
• Add in two sizes and versions.
• One add with size 95 mm x 128 mm
• One add with size 192 x 128 mm
• We want one add as a teaser before the clinic is opening. The add a bit faded and the text "Öppnar i November" across the add on the side. And one version of the add without "Öppnar i November"

```html
<!DOCTYPE html>
<html lang="sv">
<head>
<meta charset="utf-8">
<title>BrovaClinic – Öppnar i November</title>
<link href="https://fonts.googleapis.com/css2?family=Roboto:ital,wght@0,400;0,500;0,700;1,400&display=swap" rel="stylesheet">
<style>
  :root {
    --teal: #33b8a4;
    --blue: #33a6d7;
    --sky: #85cae6;
    --ink: #1a1a1a;
    --slate: #5d6670;
    --paper: #ffffff;
  }
  html, body {
    margin: 0;
    padding: 0;
    overflow: hidden;
    background: var(--paper);
  }
  .ad {
    position: relative;
    width: 900px;
    height: 1200px;
    overflow: hidden;
    background: var(--paper);
    font-family: "Roboto", Arial, sans-serif;
  }
  .hero-photo {
    position: absolute;
    left: 0; top: 0;
    width: 900px; height: 620px;
    background:
      radial-gradient(ellipse at 78% 45%, #d9c8e6 0%, rgba(217,200,230,0) 45%),
      radial-gradient(ellipse at 42% 52%, #f1b3a8 0%, rgba(241,179,168,0) 30%),
      radial-gradient(ellipse at 18% 60%, #eef0f2 0%, rgba(238,240,242,0) 55%),
      linear-gradient(180deg, #f4f5f7 0%, #e9ebee 70%, #f7f7f7 100%);
  }
  .accent-band {
    position: absolute;
    top: 620px; left: 0;
    width: 900px; height: 12px;
    display: flex;
  }
  .accent-band .band-deep { width: 451px; background: var(--blue); }
  .accent-band .band-light { flex: 1; background: var(--sky); }

  .opening-sign {
    position: absolute;
    left: 116px; top: 668px;
    width: 671px; height: 107px;
  }
  .opening-sign svg { position: absolute; inset: 0; }
  .opening-title {
    position: absolute;
    inset: 0;
    margin: 0;
    display: flex;
    align-items: center;
    justify-content: center;
    color: var(--teal);
    font-weight: 700;
    font-size: 70px;
    letter-spacing: 0.5px;
    line-height: 1;
  }
  .clinic-subtitle {
    position: absolute;
    top: 808px; left: 0; width: 900px;
    margin: 0;
    text-align: center;
    color: var(--ink);
    font-weight: 400;
    font-size: 28px;
  }
  .services {
    position: absolute;
    top: 862px; left: 0; width: 900px;
    margin: 0;
    text-align: center;
    color: var(--blue);
    font-size: 21px;
  }
  .info-box {
    position: absolute;
    left: 34px; top: 982px;
    width: 423px; height: 183px;
    background: var(--teal);
    color: var(--paper);
    box-sizing: border-box;
    padding: 17px 16px 0 14px;
  }
  .info-lead {
    margin: 0 0 0 14px;
    font-style: italic;
    font-size: 18px;
  }
  .info-url {
    margin: 10px 0 8px 56px;
    font-size: 24px;
    font-weight: 400;
  }
  .info-directions {
    margin: 0;
    font-style: italic;
    font-size: 17.5px;
    line-height: 1.32;
  }
  .brand {
    position: absolute;
    left: 545px; top: 1062px;
    width: 320px;
  }
  .brand-name {
    display: flex;
    align-items: center;
    gap: 10px;
    color: var(--slate);
    font-size: 50px;
    font-weight: 500;
    line-height: 1;
  }
  .brand-mark {
    width: 30px; height: 30px;
    background: var(--teal);
    flex: none;
  }
  .brand-tagline {
    margin: 6px 0 0 4px;
    color: var(--blue);
    font-size: 19px;
    font-weight: 500;
  }
</style>
</head>
<body>
  <main class="ad">
    <div class="hero-photo" role="img" aria-label="Photo: a doctor listens with a stethoscope to a white teddy bear held by a young girl, with her mother beside them at a desk"></div>

    <div class="accent-band">
      <div class="band-deep"></div>
      <div class="band-light"></div>
    </div>

    <div class="opening-sign">
      <svg width="671" height="107" viewBox="0 0 671 107" fill="none" stroke="#33b8a4" stroke-width="2.5">
        <polyline points="1,106 1,1 670,1 670,106"/>
        <line x1="1" y1="106" x2="42" y2="106"/>
        <line x1="629" y1="106" x2="670" y2="106"/>
      </svg>
      <h1 class="opening-title">Öppnar i November</h1>
    </div>

    <p class="clinic-subtitle">Skandinavisk Vårdcentral Costa Blanca</p>
    <p class="services">Hembesök/Mobil Vårdcentral | Lättakut | Uppföljning av blodtryck, diabetes</p>

    <section class="info-box">
      <p class="info-lead">Read more and book your time easily at</p>
      <p class="info-url">www.brovaclinic-demo.com</p>
      <p class="info-directions">Hitta hit:<br>
        Kliniken ligger utmed N418 vid Playa Serenita,<br>
        mitt emot Lorvista<br>
        Av. Tomás Herrera 7-2, 03412 Valmira Costa</p>
    </section>

    <div class="brand">
      <div class="brand-name">BrovaClinic<span class="brand-mark"></span></div>
      <p class="brand-tagline">Skandinavisk Läkarmottagning</p>
    </div>
  </main>
</body>
</html>
```